Website design for Harbor Bolts. ( Lock company)

Harbor Bolts is a New York Based Company that manufactures a variety of high quality Locks which sell worldwide.

Our website: We need a 'face' on the Internet , a website that tells you who we are and what we do - 'An Identity'.

it is not an eCommerce website . the website is to show customers and potential distributers who we are and what we manufacture ( so they come away with a great impression of our company and our products) see www.quarrelwheel.com

First glance impression: We are Professional; are locks are strong,and reliable. and we are ready to compete with other major Lock companies

Content: for starters the site will contain general information and background about our company (our story), were to buy our products, contact information, and display images of our Locks (and of course all the classic links including to all the legal and technical information). as time goes on we will add more features to the website i.e. Products, Videos blogs etc.

although at first there will not be that much content on the website - it should not look empty (it should be simple and clear but not empty) it should look and feel like a full fledged professional website (not a template)

Inspiration: here are a few sites which have the feel we are looking for:

General tone - quarrelwheel.com bramhold.com (black is good - But not a must )

Simplicity, clarity - coldvane.com panwright.com

the widescreen Image look - http://www.pagecritter.com/demo/58261.html

we are considering perhaps having wide HQ images of Lion(s) in the background (but without the felling that it is a zoo or safari website) - it is not a must, its just an idea .

perhaps (if you find it looks good ) use a bit of that metal or chrome look to give it it a strong smooth feel (however it should not look like a dark prison)

We do not currently have a Logo ( if you feel you can design one that fits the above company description - we would love to see if it can work for us) We can talk about additional funds for the logo during this project.

Our working slogan is : Harbor Bolts - "Keeper of your Ground"

for your convenience we have attached a few images of the type of locks we sell

We are looking to collaborate with you throughout the project. We have ideas and visions we want implemented and we will help you along the way. So we can create the perfect website.

Thank you.

```html
<!DOCTYPE html>
<html lang="en">
<head>
<meta charset="utf-8">
<title>Harbor Bolts - Keeper of your Ground</title>
<link href="https://fonts.googleapis.com/css2?family=Bebas+Neue&family=Oswald:wght@300;400&display=swap" rel="stylesheet">
<style>
:root{
  --red:#c3151b;
  --red-band:#a80a0c;
  --black:#000;
  --header:#151515;
  --slate:#2e3135;
  --grey-text:#8a8d91;
  --light:#dcdcdc;
  --logo:#b9bbbf;
  --footer:#1b1b1b;
  --display:'Bebas Neue',Impact,sans-serif;
  --cond:'Oswald','Arial Narrow',sans-serif;
  --body:Arial,Helvetica,sans-serif;
}
*{box-sizing:border-box;margin:0;padding:0}
html,body{width:1093px;height:1200px;overflow:hidden;background:var(--black);font-family:var(--body)}
.page{position:relative;width:1093px;height:1200px}
.abs{position:absolute}

.topline{left:0;top:0;width:1093px;height:6px;background:var(--red)}
.topline-notch{left:665px;top:6px;width:0;height:0;border-left:8px solid transparent;border-right:8px solid transparent;border-top:7px solid var(--red)}
.site-header{left:0;top:6px;width:1093px;height:61px;background:linear-gradient(#2a2a2a,#0c0c0c);border-bottom:1px solid #333}
.brand{display:flex;align-items:center;gap:8px}
.brand-dot{width:26px;height:26px;border-radius:50%;background:var(--logo)}
.brand-name{font-family:var(--display);font-size:38px;color:var(--logo);letter-spacing:.5px;line-height:1}
.site-header .brand{position:absolute;left:120px;top:13px}
.nav{position:absolute;right:105px;top:21px;display:flex;gap:14px;font-family:var(--cond);font-weight:400;font-size:15px;color:#e3e3e3;text-transform:uppercase;letter-spacing:.2px}

.hero{left:0;top:67px;width:1093px;height:391px;background:radial-gradient(ellipse at 80% 50%,#6b4f2c 0%,#3a2c1c 35%,#1e1a16 65%,#121212 100%)}
.hero-lock{left:501px;top:126px;width:90px;height:90px}
.hero-title{left:0;top:218px;width:1093px;text-align:center;font-family:var(--display);font-size:124px;line-height:1;color:var(--light)}
.slogan{left:354px;top:343px;width:389px;height:49px;background:var(--light);font-family:var(--display);font-size:50px;line-height:52px;text-align:center;color:#0a0a0a}

.products-band{left:0;top:458px;width:1093px;height:278px;background:var(--slate)}
.products{left:141px;top:476px;width:814px;height:241px;background:var(--black);display:flex;padding:0 10px}
.product{width:203px;padding:20px 20px 0}
.product-img{width:150px;height:118px;margin:0 auto;border-radius:6px}
.img-knob{background:radial-gradient(circle at 50% 50%,#e8c77a,#a07a3a 55%,#000 72%)}
.img-box{background:radial-gradient(ellipse at 50% 55%,#3a3a3a,#1a1a1a 40%,#000 65%)}
.product h3{font-family:var(--display);font-weight:400;font-size:24px;color:var(--red);text-align:center;margin-top:7px;line-height:1}
.product p{font-size:11px;line-height:13.5px;color:var(--grey-text);margin-top:6px}
.arrow{width:32px;height:32px}

.welcome h2{left:128px;top:812px;font-family:var(--display);font-weight:400;font-size:48px;color:var(--grey-text);line-height:1}
.welcome-text{left:128px;top:870px;width:220px;font-size:12.5px;line-height:15.5px;color:var(--grey-text)}
.read-more{left:128px;top:962px;font-size:12.5px;color:#ccc}
.update{width:290px;height:90px}
.update-date{position:absolute;left:0;top:0;width:81px;height:81px;border:2px solid #3a3a3a;border-radius:50%;color:#bfbfbf;font-size:16px;display:flex;align-items:center;justify-content:center}
.update-body{position:absolute;left:97px;top:7px;width:200px;font-size:11.5px;line-height:14.5px;color:var(--grey-text)}
.update-body strong{display:block;font-weight:400;font-size:13px;color:#c6c6c6;margin-bottom:3px}
.rule{height:1px;background:#333}
.more-updates{right:115px;top:941px;font-size:12px;color:#ccc}

.mail-band{left:0;top:1045px;width:1093px;height:73px;background:var(--red-band)}
.mail-band .brand{position:absolute;left:120px;top:20px}
.mail-title{left:493px;top:19px;font-family:var(--cond);font-weight:300;font-size:30px;color:#e9d5d5;line-height:1;letter-spacing:-.5px}
.mail-form{left:730px;top:19px;width:246px;height:38px;border:2px solid #7d0608;background:#7d0608;display:flex}
.mail-input{flex:1;background:#8a0709;color:#d37a7a;font-size:13px;padding:11px 10px}
.mail-go{width:60px;background:var(--red);font-family:var(--display);font-size:28px;color:#fff;text-align:center;line-height:36px}

.site-footer{left:0;top:1118px;width:1093px;height:82px;background:var(--footer)}
.footer-links{position:absolute;left:120px;top:38px;display:flex;gap:12px;font-size:11.5px;color:#a9a9a9}
.social{position:absolute;left:816px;top:32px;display:flex;gap:8px}
.social span{width:25px;height:25px;border-radius:50%;background:#9c9c9c}
</style>
</head>
<body>
<div class="page">
  <div class="abs topline"></div>
  <header class="abs site-header">
    <div class="brand"><span class="brand-dot"></span><span class="brand-name">Harbor Bolts</span></div>
    <nav class="nav"><span>Home</span><span>About Us</span><span>Products</span><span>Services</span><span>Blog</span><span>Contact Us</span></nav>
  </header>
  <div class="abs topline-notch"></div>

  <section class="abs hero" role="img" aria-label="Wide dark photograph of a lion in profile"></section>
  <svg class="abs hero-lock" viewBox="0 0 90 90" aria-hidden="true">
    <circle cx="45" cy="45" r="43" fill="none" stroke="#ddd" stroke-width="3"/>
    <path d="M35 41v-8a10 10 0 0 1 20 0" fill="none" stroke="#ddd" stroke-width="5"/>
    <rect x="30" y="41" width="30" height="24" rx="3" fill="#ddd"/>
    <rect x="43" y="48" width="4" height="10" fill="#222"/>
  </svg>
  <h1 class="abs hero-title">HARBOR BOLTS</h1>
  <div class="abs slogan">KEEPER OF YOUR GROUND</div>

  <div class="abs products-band"></div>
  <section class="abs products">
    <article class="product"><div class="product-img img-knob" role="img" aria-label="Brass entry lock knob with key"></div><h3>ENTRY LOCK</h3><p>Lorem ipsum dolor sit amet, consectetur adipisicing elit, sed do eiusmod tempor incididunt ut.</p></article>
    <article class="product"><div class="product-img img-box" role="img" aria-label="Black combination lockbox with shackle"></div><h3>LOCKBOX</h3><p>Lorem ipsum dolor sit amet, consectetur adipisicing elit, sed do eiusmod tempor incididunt ut.</p></article>
    <article class="product"><div class="product-img img-knob" role="img" aria-label="Brass entry lock knob with key"></div><h3>ENTRY LOCK</h3><p>Lorem ipsum dolor sit amet, consectetur adipisicing elit, sed do eiusmod tempor incididunt ut.</p></article>
    <article class="product"><div class="product-img img-box" role="img" aria-label="Black combination lockbox with shackle"></div><h3>LOCKBOX</h3><p>Lorem ipsum dolor sit amet, consectetur adipisicing elit, sed do eiusmod tempor incididunt ut.</p></article>
  </section>
  <svg class="abs arrow" style="left:104px;top:582px" viewBox="0 0 32 32" aria-label="Previous"><circle cx="16" cy="16" r="14" fill="none" stroke="#000" stroke-width="3"/><path d="M18 9l-7 7 7 7" fill="none" stroke="#000" stroke-width="3"/></svg>
  <svg class="abs arrow" style="left:960px;top:582px" viewBox="0 0 32 32" aria-label="Next"><circle cx="16" cy="16" r="14" fill="none" stroke="#000" stroke-width="3"/><path d="M14 9l7 7-7 7" fill="none" stroke="#000" stroke-width="3"/></svg>

  <section class="welcome">
    <h2 class="abs">WELCOME</h2>
    <p class="abs welcome-text">Mes cuml dia sed in lacus ut eniascet ingerto aliiqt es site amet eismod ictor ut ligulate ameti dapibus ticdu nt mtsen lusto dolor ltissim com. Mes cuml dia sed inertio.</p>
    <a class="abs read-more">read more +</a>
    <div class="abs update" style="left:379px;top:820px"><div class="update-date">16.04</div><div class="update-body"><strong>Ut enim ad minim veniam, quis</strong>Excepteur sint occaecat cupidatat non proident, sunt in culpa qui officia eserunt mollit anim id est laborum.</div></div>
    <div class="abs update" style="left:694px;top:820px"><div class="update-date">16.04</div><div class="update-body"><strong>Ut enim ad minim veniam, quis</strong>Excepteur sint occaecat cupidatat non proident, sunt in culpa qui officia eserunt mollit anim id est laborum.</div></div>
    <div class="abs rule" style="left:383px;top:926px;width:279px"></div>
    <div class="abs rule" style="left:698px;top:926px;width:279px"></div>
    <a class="abs more-updates">+ more updates</a>
  </section>

  <section class="abs mail-band">
    <div class="brand"><span class="brand-dot"></span><span class="brand-name">Harbor Bolts</span></div>
    <h2 class="abs mail-title">JOIN OUR MAILING LIST</h2>
    <div class="abs mail-form"><span class="mail-input">Example@email.com</span><span class="mail-go">GO</span></div>
  </section>

  <footer class="abs site-footer">
    <nav class="footer-links"><span>Home</span><span>About Us</span><span>Products</span><span>Services</span><span>Blog</span><span>Contact</span><span>Legal</span><span>Privacy Policy</span><span>©2013 Northgate Hardware, Inc.</span></nav>
    <div class="social"><span></span><span></span><span></span><span></span><span></span></div>
  </footer>
</div>
</body>
</html>
```